Product sheet for managing talented people!

We need a new product sheet to describe our method of helping organisations to manage their talented people! We have selected a rowing team as the graphical theme (sample attached - please select or suggest a new picture if you want). We have also attached a powerpoint slide with our model (this is the service we offer).

FRONT PAGE

We are looking for an eye-catching front page that uses our 1. "Kestrel Growth Model"; 2. a picture of a rowing team of 8, and 3. our logo and 1800 KESTRL phone number (1800 537 875).

Step 1 - Assess key positions to determine your Talent Management Priorities.

Step 2 - Organisational psychology support helps individuals self-evaluate (see page 2 for details).

Step 3 - Facilitate agreement with manager and embed best-practice in organisational fairness.

Step 4 - Tailor career development and redeployment options based on shared understanding.

Step 5 - Evaluate ROI for individual performance and engagement.

BACK PAGE

The second page will have more detail of each of the talent categories also included in the powerpoint slide. Logo attached also. Please also view our website as the graphics should give you a sense of the look and feel of our brand - www.kestrelgm.com.au We have also added another flyer that we still use - please do not reverse the logo on this project - use in current form. CORPORATE LOGO / COLOUR GUIDE
C100 M50 Y0 K0
C100 M50 Y0 K0
C100 M50 Y0 K0
Gradient
C100 M60 Y0 K40
C100 M45 Y0 K0
C100 M20 Y0 K0
C70 M0 Y0 K0
PMS 2935 C
PMS 2935 C 75% Tint
PMS 2935 C
PMS Process Cyan C

The successful flyer will need to be print ready (as per attached example) and in pdf form so that we can print and/or send as a PDF.

Thanks.

Target Market(s)

Human Resource Managers in business and government.

Industry/Entity Type

Product

Requirements
Must have
• Eye-catching graphics with a rowing team theme. Colours consistent with our corporate colour codes.
Nice to have
• Please add small "trademark" symbol to the logo. This is small TM in a circle and usually placed at top right hand of logo. PLease add our website address www.kestrelgm.com
Should not have
• Please do not "reverse" the logo - use as is.

```html
<!DOCTYPE html>
<html lang="en">
<head>
<meta charset="utf-8">
<title>Kestrel Growth Model – Product Sheet</title>
<link rel="stylesheet" href="https://fonts.googleapis.com/css2?family=Lato:ital,wght@0,400;0,700;0,900;1,400;1,700&family=Oswald:wght@600&display=swap">
<style>
:root{
  --bg:#e8e6e3;
  --paper:#ffffff;
  --blue:#0a6fc2;
  --blue-deep:#005a9e;
  --indigo:#3d4a9e;
  --charcoal:#3a3a3c;
  --ink:#1d1d1f;
  --panel-grey:#f1f2f4;
}
*{margin:0;padding:0;box-sizing:border-box}
html,body{width:1050px;height:1200px;overflow:hidden;background:var(--bg)}
body{font-family:"Lato",sans-serif;position:relative}
.sheet{position:absolute;left:125px;top:38px;width:795px;height:1116px;background:var(--paper);box-shadow:0 4px 14px rgba(0,0,0,.25);overflow:hidden}
.sheet-art{position:absolute;inset:0;width:795px;height:1116px}
.brand{position:absolute;left:548px;top:62px;width:180px;text-align:center;color:var(--indigo);font-weight:400}
.brand-name{display:block;font-size:36px;letter-spacing:2px;line-height:1}
.brand-tag{display:block;font-size:8.5px;letter-spacing:1.6px;margin-top:6px}
.model-title{position:absolute;left:29px;top:642px;font-weight:900;font-size:25px;color:var(--ink);letter-spacing:.2px;white-space:nowrap}
.model-title .accent{color:var(--blue)}
.category{position:absolute;left:29px;display:flex;align-items:center}
.category-tag{height:25px;background:var(--blue);color:#fff;font-weight:700;font-size:15px;line-height:25px;padding:0 14px 0 16px;box-shadow:0 4px 5px -2px rgba(0,0,0,.35)}
.category-note{position:absolute;left:143px;width:200px;font-style:italic;font-weight:700;font-size:12px;color:var(--ink);line-height:1.2}
.step{position:absolute;left:411px;width:362px}
.step-tag{display:inline-block;background:#fff;color:var(--ink);font-weight:700;font-size:15px;height:24px;line-height:24px;padding:0 30px 0 14px}
.step-text{margin-top:10px;color:#fff;font-style:italic;font-size:13px;line-height:1.32}
.phone{position:absolute;left:306px;top:1048px;display:flex;align-items:center;gap:14px;color:#fff}
.phone-icon{width:36px;height:36px}
.phone-number{font-family:"Oswald",sans-serif;font-weight:600;font-size:31px;letter-spacing:.5px;white-space:nowrap}
</style>
</head>
<body>
<main class="sheet">
  <svg class="sheet-art" viewBox="0 0 795 1116" aria-hidden="false">
    <defs>
      <linearGradient id="photoTone" x1="0" y1="0" x2="0.25" y2="1">
        <stop offset="0" stop-color="#2f4a23"/>
        <stop offset="0.28" stop-color="#8a9a86"/>
        <stop offset="0.5" stop-color="#e8e6e6"/>
        <stop offset="0.75" stop-color="#c9a08a"/>
        <stop offset="1" stop-color="#5d5a58"/>
      </linearGradient>
      <linearGradient id="leftPanel" x1="0" y1="0" x2="1" y2="0">
        <stop offset="0" stop-color="#ffffff"/>
        <stop offset="1" stop-color="var(--panel-grey)"/>
      </linearGradient>
      <linearGradient id="rightPanel" x1="0" y1="0" x2="0" y2="1">
        <stop offset="0" stop-color="#0b74c6"/>
        <stop offset="1" stop-color="#0561ad"/>
      </linearGradient>
    </defs>

    <path role="img" aria-label="Photo: a women's rowing crew pulling oars in unison on a river" d="M0 205 C90 170 170 95 219 12 C310 95 540 190 795 210 L795 610 C560 565 260 580 0 640 Z" fill="url(#photoTone)"/>

    <path d="M0 196 C85 160 170 80 219 6 L226 22 C180 100 95 190 0 232 Z" fill="var(--blue)"/>
    <path d="M0 200 C85 168 168 92 218 14 L221 20 C172 100 90 178 0 214 Z" fill="var(--charcoal)"/>
    <path d="M219 6 C320 95 560 160 795 168 L795 190 C560 182 320 122 219 6 Z" fill="var(--charcoal)"/>
    <path d="M236 28 C360 128 580 196 795 198 L795 222 C570 218 330 150 236 28 Z" fill="var(--blue)"/>

    <rect x="0" y="620" width="382" height="420" fill="url(#leftPanel)"/>
    <rect x="382" y="600" width="413" height="440" fill="url(#rightPanel)"/>
    <path d="M0 612 C240 560 560 555 795 602 L795 630 C560 585 250 592 0 660 Z" fill="var(--blue)"/>
    <path d="M0 650 C250 588 560 582 795 626 L795 634 C560 592 255 600 0 660 Z" fill="#ffffff" opacity=".9"/>
    <path d="M560 586 C680 600 760 640 795 670 L795 688 C740 650 660 610 560 586 Z" fill="var(--charcoal)"/>

    <path d="M0 1035 C250 1000 560 995 795 1018 L795 1050 C560 1030 300 1040 0 1080 Z" fill="var(--blue)"/>
    <path d="M0 1078 C300 1040 560 1030 795 1048 L795 1054 C560 1037 300 1048 0 1086 Z" fill="#ffffff"/>
    <path d="M0 1084 C300 1046 560 1036 795 1052 L795 1116 L0 1116 Z" fill="var(--charcoal)"/>
  </svg>

  <div class="brand">
    <span class="brand-name">KESTREL</span>
    <span class="brand-tag">GROWTH MANAGEMENT</span>
  </div>

  <h1 class="model-title">KESTREL GROWTH <span class="accent">MODEL</span></h1>

  <div class="category" style="top:703px"><span class="category-tag">Exit</span></div>
  <p class="category-note" style="top:708px;left:172px">: Planned or managed</p>
  <div class="category" style="top:756px"><span class="category-tag">Developing</span></div>
  <p class="category-note" style="top:761px;left:172px">: High risk/high reward</p>
  <div class="category" style="top:809px"><span class="category-tag">Contributing</span></div>
  <p class="category-note" style="top:814px;left:172px">: Probable flight risk</p>
  <div class="category" style="top:863px"><span class="category-tag">Emerging</span></div>
  <p class="category-note" style="top:868px;left:172px">: Manage career aspirations</p>
  <div class="category" style="top:919px"><span class="category-tag">Elite</span></div>
  <p class="category-note" style="top:924px;left:172px">: Mission critical or market-sensitive</p>
  <div class="category" style="top:975px"><span class="category-tag">Target</span></div>
  <p class="category-note" style="top:976px;left:172px">: Strategic external hire with<br>&nbsp;&nbsp;market implications</p>

  <div class="step" style="top:626px"><span class="step-tag">Step 1</span><p class="step-text">Assess key positions to determine your Talent Management Priorities.</p></div>
  <div class="step" style="top:707px"><span class="step-tag">Step 2</span><p class="step-text">Organisational psychology support helps individuals self-evaluate (see page 2 for details)</p></div>
  <div class="step" style="top:788px"><span class="step-tag">Step 3</span><p class="step-text">Facilitate agreement with manager and embed best-practice in organisational fairness.</p></div>
  <div class="step" style="top:867px"><span class="step-tag">Step 4</span><p class="step-text">Tailor career development and redeployment options based on shared understanding.</p></div>
  <div class="step" style="top:944px"><span class="step-tag">Step 5</span><p class="step-text">Evaluate ROI for individual performance and engagement.</p></div>

  <div class="phone">
    <svg class="phone-icon" viewBox="0 0 36 36" aria-hidden="true">
      <circle cx="18" cy="18" r="16" fill="none" stroke="#fff" stroke-width="2.2"/>
      <path d="M13.2 9.5c.7-.4 1.5-.2 1.9.5l1.6 2.8c.4.7.2 1.5-.4 1.9l-1.3.9c.7 2.4 2.5 4.6 4.6 5.8l1.2-1c.6-.5 1.5-.5 2 .1l2.2 2.3c.6.6.6 1.5 0 2.1l-1.2 1.2c-1 1-2.6 1.2-3.9.6-4.6-2.2-8-6.8-8.7-11.8-.2-1.4.4-2.8 1.6-3.6z" fill="#fff"/>
    </svg>
    <span class="phone-number">1800 KESTRL (1800 537 875)</span>
  </div>
</main>
</body>
</html>
```